Personal Finance Author needs a postcard

Hi there,

I am a Canadian personal finance author and have published a new book called The Wealth Compass.

I teach Millennials how to create a 6-figure portfolio through investing (https://www.dariafelt.com/)

I'm speaking at some conferences so we were going to print some postcards to hand out to attendees with our info and calls-to-action on them.

I am looking for 4x6 (horizontal) postcard (no space needed for shipping label).

Logos, Headshots and Book Cover:
https://files.cloudvaultex.com/folders/8kQpZrT2mWvN4xLbJ7sHdYc3FgA9eUoRi?usp=sharing

Both sides will be full colour. I would like a clean and simple look. Our main sites are www.DariaFelt.com and www.TheWealthCompassBook.com if you want to get a sense of style and design.
I also uploaded a few marketing materials so you can see the existing designs.

Side 1:
Get Instant Access to your Free Resources - main headline

(small bullets underneath)
- The Wealth Compass Checklist
- Financial Worksheets
- Database of Investment Tools

DariaFelt.com/Resources

At the bottom, include "Don't forget to follow Daria Felt on social media:
Linkedin: @dariafelt7
Facebook: @thewealthcompassbook Instagram: @thewealthcompassbook Twitter: @WealthCompassBk"

Side 2:
Headline - Want to work directly with Daria and The Wealth Compass team to help you make your money grow and stay safe?

Work with us to (bullet point list)...
- Hire Daria as a Keynote Speaker
- Teach Financial Literacy Workshops
- Receive Financial Coaching

Want To Learn More About How We Can Help?
DariaFelt.com/Services

Include my contact info:
Daria Felt
Author | Speaker | Investor
daria@thewealthcompassbook.com
416-555-0187

Target Market(s)

Millennials who want to learn how to save and invest their money. I focus on stock market investing, real estate investing and entrepreneurship.

Industry/Entity Type

Financial Service

Font styles to use
Sans Serif

Colors

Designer to choose colors to be used in the design.

Requirements
Must have
• Photo of Daria Felt
• The Wealth Compass logo
• Green, Gold/Yellow to match existing colours
• modern business style postcard

```html
<!DOCTYPE html>
<html lang="en">
<head>
<meta charset="utf-8">
<title>The Wealth Compass – Postcard</title>
<link rel="stylesheet" href="https://fonts.googleapis.com/css2?family=Oswald:wght@600;700&family=Questrial&family=Poppins:wght@700&family=Marcellus+SC&display=swap">
<style>
  :root {
    --green: #14693a;
    --gold: #e8a92a;
    --gold-light: #f1d27a;
    --ink: #1f1f1f;
    --white: #ffffff;
    --backdrop: #cfcdce;
  }
  * { box-sizing: border-box; margin: 0; padding: 0; }
  html, body { width: 848px; height: 1200px; overflow: hidden; }
  body { background: var(--backdrop); position: relative; font-family: "Questrial", sans-serif; }

  .postcard {
    position: absolute; left: 172px; width: 503px; height: 335px;
    background: var(--white); overflow: hidden;
    box-shadow: 0 2px 6px rgba(0,0,0,.25);
  }
  .postcard--front { top: 22px; }
  .postcard--back { top: 388px; background: var(--green); }

  /* Front */
  .accent-bar { position: absolute; left: 0; top: 25px; width: 13px; height: 99px; background: var(--gold); }
  .headline {
    position: absolute; left: 22px; top: 22px;
    font-family: "Oswald", sans-serif; font-weight: 700; color: var(--green);
    font-size: 29.5px; line-height: 25.6px; text-transform: uppercase; letter-spacing: .4px;
  }
  .resource-link {
    position: absolute; left: 22px; top: 133px;
    font-family: "Oswald", sans-serif; font-weight: 600; color: var(--gold);
    font-size: 14px; padding-bottom: 1px; border-bottom: 1.5px solid var(--gold);
  }
  .bullet-list { position: absolute; list-style: none; font-size: 11px; line-height: 13px; color: var(--ink); }
  .bullet-list li::before { content: "•"; margin-right: 6px; }
  .front-bullets { left: 22px; top: 160px; }

  .wave { position: absolute; left: 0; top: 0; }

  .social-list { position: absolute; left: 21px; top: 270px; list-style: none; font-size: 8.5px; line-height: 13px; color: var(--white); }
  .social-list li { display: flex; align-items: center; gap: 5px; }
  .social-list .mark { width: 8px; height: 8px; background: var(--white); display: inline-block; }

  .brand-name {
    position: absolute; left: 282px; top: 44px; width: 200px;
    display: flex; align-items: center; justify-content: center; gap: 8px;
    font-family: "Questrial", sans-serif; font-size: 25px; line-height: 30px;
    color: var(--green); text-align: left;
  }
  .brand-name__dot { width: 14px; height: 14px; border-radius: 50%; background: var(--gold); flex: none; }

  .portrait {
    position: absolute; left: 364px; top: 142px; width: 138px; height: 193px;
    border-radius: 60px 60px 0 0;
    background: linear-gradient(180deg, #d9b79a 0%, #c89a78 35%, #2a2a30 55%, #1b1b22 100%);
  }

  .follow-seal {
    position: absolute; left: 198px; top: 191px; width: 102px; height: 102px; border-radius: 50%;
    background: radial-gradient(circle at 35% 30%, #fbeec2 0%, var(--gold-light) 45%, #c99a3a 100%);
    display: flex; flex-direction: column; justify-content: center; align-items: center;
    text-align: center; font-size: 8px; line-height: 12px; color: var(--ink);
  }
  .follow-seal strong { font-family: "Poppins", sans-serif; font-weight: 700; color: var(--green); font-size: 10px; }

  /* Back */
  .money-banner {
    position: absolute; left: 0; top: 0; width: 503px; height: 140px;
    background: linear-gradient(120deg, #f3f4f1 0%, #e2e6df 40%, #eef0ec 70%, #dfe3dc 100%);
  }
  .back-headline {
    position: absolute; left: 0; top: 20px; width: 503px; text-align: center;
    font-family: "Poppins", sans-serif; font-weight: 700; color: var(--green);
    font-size: 18.5px; line-height: 22px;
  }
  .back-rule { position: absolute; left: 144px; top: 117px; width: 214px; height: 1px; background: var(--green); }
  .gold-band { position: absolute; left: 0; top: 139px; width: 503px; height: 6px; background: var(--gold); }
  .pointer { position: absolute; width: 0; height: 0; border-left: 8px solid transparent; border-right: 8px solid transparent; border-top: 12px solid var(--white); }
  .pointer--band { left: 21px; top: 145px; }
  .pointer--cta { left: 91px; top: 282px; border-left-width: 7px; border-right-width: 7px; border-top-width: 11px; }
  .back-bullets { left: 22px; top: 164px; color: var(--white); font-size: 11px; line-height: 12.6px; }

  .cta {
    position: absolute; left: 22px; top: 214px; width: 152px;
    font-family: "Oswald", sans-serif; font-weight: 600; text-transform: uppercase; color: var(--white); line-height: 1;
  }
  .cta__line1 { font-size: 20px; }
  .cta__line2 { font-size: 25px; color: var(--gold); }
  .cta__line3 { font-size: 17px; }
  .services-link {
    position: absolute; left: 22px; top: 297px;
    font-family: "Oswald", sans-serif; font-weight: 600; color: var(--gold); font-size: 14.5px;
  }

  .contact { position: absolute; right: 22px; top: 166px; text-align: right; color: var(--white); }
  .contact__name { font-family: "Marcellus SC", serif; font-size: 19px; line-height: 20px; letter-spacing: .5px; }
  .contact__role { font-size: 12px; line-height: 14px; }
  .contact__line { display: flex; justify-content: flex-end; align-items: center; gap: 4px; font-size: 10.5px; line-height: 16px; }
  .contact__details { margin-top: 13px; }
  .contact__line svg { width: 11px; height: 11px; }
</style>
</head>
<body>

<section class="postcard postcard--front">
  <svg class="wave" width="503" height="335" viewBox="0 0 503 335" aria-hidden="true">
    <path d="M0,254 Q240,212 503,252 L503,335 L0,335 Z" fill="var(--gold)"/>
    <path d="M0,260 Q240,219 503,259 L503,335 L0,335 Z" fill="var(--green)"/>
  </svg>

  <div class="accent-bar"></div>
  <h1 class="headline">Get Instant<br>Access to<br>Your Free<br>Resources</h1>
  <div class="resource-link">DariaFelt.com/Resources</div>
  <ul class="bullet-list front-bullets">
    <li>The Wealth Compass Checklist</li>
    <li>Financial Worksheets</li>
    <li>Database of Investment Tools</li>
  </ul>

  <div class="brand-name">
    <span class="brand-name__dot"></span>
    <span>The Wealth<br>Compass</span>
  </div>

  <div class="portrait" role="img" aria-label="Photo of Daria Felt, smiling, in a dark blazer with hand on hip"></div>

  <div class="follow-seal">
    <span>Don't forget</span>
    <span>to follow</span>
    <strong>Daria Felt</strong>
    <span>on social media:</span>
  </div>

  <ul class="social-list">
    <li><span class="mark"></span>@dariafelt7</li>
    <li><span class="mark"></span>@thewealthcompassbook</li>
    <li><span class="mark"></span>@thewealthcompassbook</li>
    <li><span class="mark"></span>@WealthCompassBk</li>
  </ul>
</section>

<section class="postcard postcard--back">
  <div class="money-banner" role="img" aria-label="Faded background of scattered banknotes"></div>
  <h2 class="back-headline">Want to work directly with Daria<br>and The Wealth Compass team<br>to help you make your money<br>grow and stay safe?</h2>
  <div class="back-rule"></div>
  <div class="gold-band"></div>
  <div class="pointer pointer--band"></div>

  <ul class="bullet-list back-bullets">
    <li>Hire Daria as a Keynote Speaker</li>
    <li>Teach Financial Literacy Workshops</li>
    <li>Receive Financial Coaching</li>
  </ul>

  <div class="cta">
    <div class="cta__line1">Want to Learn</div>
    <div class="cta__line2">More About</div>
    <div class="cta__line3">How We Can Help?</div>
  </div>
  <div class="pointer pointer--cta"></div>
  <div class="services-link">DariaFelt.com/Services</div>

  <div class="contact">
    <div class="contact__name">Daria Felt</div>
    <div class="contact__role">Author &nbsp;|&nbsp; Speaker &nbsp;|&nbsp; Investor</div>
    <div class="contact__details">
      <div class="contact__line">daria@thewealthcompassbook.com
        <svg viewBox="0 0 12 12" aria-hidden="true"><rect x="1" y="3" width="10" height="7" fill="none" stroke="#fff" stroke-width="1.2"/><path d="M1,3 L6,7 L11,3" fill="none" stroke="#fff" stroke-width="1.2"/></svg>
      </div>
      <div class="contact__line">416-555-0187
        <svg viewBox="0 0 12 12" aria-hidden="true"><path d="M1,4 Q6,0 11,4 L9,5.5 L8,4 L4,4 L3,5.5 Z" fill="#fff"/><rect x="2.5" y="6" width="7" height="5" rx="1" fill="#fff"/></svg>
      </div>
    </div>
  </div>
</section>

</body>
</html>
```